Business Card Design

Business Card for professional consulting firm working with large financial institutions.

Target Market(s)

Executive buyers

Industry/Entity Type

Banking

Contact Information for Business Card

Mild creativity wanted. Not boring, but do elaborate artwork.

Font styles to use
Serif
Sans Serif

Colors

Designer to choose colors to be used in the design.

Requirements
Must have
• Standard business card features - company name, individual name, telephone, website, email, locations.
Nice to have
• Two colors
Should not have
• too many colors, fancy printing, cartoons.

```html
<!DOCTYPE html>
<html lang="en">
<head>
<meta charset="utf-8">
<title>Halcrest Partners — Business Card</title>
<link rel="stylesheet" href="https://fonts.googleapis.com/css2?family=Lora:wght@400&family=PT+Sans:wght@700&display=swap">
<style>
  :root {
    --backdrop: #e6e6e6;
    --card-dark: #2b2b2b;
    --card-dark-edge: #4a4a4a;
    --card-light: #f7f7f7;
    --ink: #3a3a3a;
    --ink-soft: #5c5c5c;
    --paper: #f2f2f2;
    --rule: #a9a9a9;
  }
  * { margin: 0; padding: 0; box-sizing: border-box; }
  html, body { width: 1200px; height: 726px; overflow: hidden; }
  body {
    background: var(--backdrop);
    display: flex;
    align-items: center;
    justify-content: center;
    gap: 60px;
    font-family: "Lora", Georgia, serif;
  }
  .card {
    position: relative;
    width: 510px;
    height: 292px;
    border-radius: 3px;
    box-shadow: 0 6px 18px rgba(0,0,0,0.18);
  }
  .card-front {
    background: linear-gradient(135deg, var(--card-dark) 0%, var(--card-dark-edge) 100%);
    display: flex;
    align-items: center;
    justify-content: center;
  }
  .brand {
    font-family: "PT Sans", Arial, sans-serif;
    font-weight: 700;
    text-transform: uppercase;
    letter-spacing: 3px;
    white-space: nowrap;
  }
  .card-front .brand { font-size: 30px; color: var(--paper); }
  .card-back { background: var(--card-light); color: var(--ink); }
  .card-back .brand {
    position: absolute;
    top: 60px;
    right: 42px;
    font-size: 22px;
    color: var(--ink);
  }
  .rule { position: absolute; height: 1px; background: var(--rule); }
  .rule-top { top: 112px; left: 250px; right: 42px; }
  .rule-name { top: 178px; left: 196px; width: 124px; }
  .person { position: absolute; left: 40px; top: 160px; }
  .person-name {
    font-family: "PT Sans", Arial, sans-serif;
    font-weight: 700;
    font-size: 21px;
    color: var(--ink);
  }
  .person-role { font-size: 13px; color: var(--ink-soft); margin-top: 2px; }
  .address {
    position: absolute;
    right: 42px;
    top: 132px;
    text-align: right;
    font-size: 13px;
    font-style: normal;
    line-height: 1.5;
    color: var(--ink);
  }
  .contacts {
    position: absolute;
    left: 40px;
    top: 218px;
    list-style: none;
    font-size: 13.5px;
    line-height: 19px;
    color: var(--ink);
  }
  .contacts li { display: flex; align-items: center; gap: 10px; }
  .contacts svg { width: 13px; height: 13px; fill: none; stroke: var(--ink); stroke-width: 1.4; }
</style>
</head>
<body>
  <section class="card card-front">
    <span class="brand">Halcrest Partners</span>
  </section>

  <section class="card card-back">
    <span class="brand">Halcrest Partners</span>
    <div class="rule rule-top"></div>

    <div class="person">
      <div class="person-name">John Doe Smith</div>
      <div class="person-role">Managing Director</div>
    </div>
    <div class="rule rule-name"></div>

    <address class="address">
      234 Anywhere St., Any City,<br>Any Town, US 123456
    </address>

    <ul class="contacts">
      <li>
        <svg viewBox="0 0 16 16"><path d="M3 2h3l1.5 3.5-2 1.2a8 8 0 0 0 3.8 3.8l1.2-2L14 10v3a1 1 0 0 1-1 1A11 11 0 0 1 2 3a1 1 0 0 1 1-1z"/></svg>
        555.555.5555
      </li>
      <li>
        <svg viewBox="0 0 16 16"><rect x="1.5" y="3.5" width="13" height="9"/><path d="M1.5 3.5 8 9l6.5-5.5"/></svg>
        johndoe@example.com
      </li>
      <li>
        <svg viewBox="0 0 16 16"><circle cx="8" cy="8" r="6.3"/><path d="M1.7 8h12.6M8 1.7c-3.5 3.5-3.5 9 0 12.6M8 1.7c3.5 3.5 3.5 9 0 12.6"/></svg>
        www.yourwebsite.com
      </li>
    </ul>
  </section>
</body>
</html>
```